Ad Banner for knowledge management portal - Promote Knowledge Submission

This banner is used in knowledge management web site.

1. Banner size: 940x380
2. Business background: Provides maintenance, design and engineering, construction, machinery operation, material procurement and production management services for petrochemical and refinery business
3. We would like to see designs that
- Promote the benefits of sharing "Lesson Learned".
- Use the keyword "I will do it better if I have to do it again"
- Promote employees to submit "Lesson Learned". It is a lesson learned from work, submitted using a predefined form template.
- Promote a campaign that will give out souvenir for all employees who submit "Lesson Learned"
- Has the message "Click here to learn more about Lesson Learned"

Requirements
Must have
• Must have a picture of technician examining machine or equipments (using cartoon character)
Should not have
• Should not include picture of real people in the design

```html
<!DOCTYPE html>
<html lang="en">
<head>
<meta charset="utf-8">
<title>Lesson Learned Banner</title>
<link rel="stylesheet" href="https://fonts.googleapis.com/css2?family=Montserrat:wght@800;900&family=Open+Sans:wght@400;600&display=swap">
<style>
  :root {
    --sky-deep: #0a93b8;
    --sky: #11a9cc;
    --sky-light: #6fd6ee;
    --glow: #d9f6ff;
    --white: #ffffff;
    --silver: #cfd6da;
    --button-top: #fff66a;
    --button-bottom: #f4c400;
    --button-edge: #d9a900;
    --cta-red: #e3202b;
    --divider: rgba(255, 255, 255, 0.45);
  }
  html, body {
    margin: 0;
    padding: 0;
    overflow: hidden;
    background: var(--white);
  }
  .banner {
    position: relative;
    width: 1200px;
    height: 484px;
    overflow: hidden;
    background:
      radial-gradient(ellipse 420px 380px at 190px 190px, var(--glow) 0%, var(--sky-light) 28%, rgba(17,169,204,0) 70%),
      linear-gradient(180deg, var(--sky) 0%, var(--sky-deep) 100%);
    font-family: "Open Sans", Arial, sans-serif;
  }
  .mascot {
    position: absolute;
    left: 55px;
    top: 25px;
    width: 455px;
    height: 459px;
    border-radius: 40px 40px 0 0;
    background: radial-gradient(ellipse at 45% 40%, rgba(255,255,255,0.35) 0%, rgba(255,255,255,0.12) 55%, rgba(255,255,255,0) 80%);
  }
  .divider {
    position: absolute;
    left: 617px;
    top: 57px;
    width: 2px;
    height: 363px;
    background: linear-gradient(180deg, rgba(255,255,255,0) 0%, var(--divider) 20%, var(--divider) 80%, rgba(255,255,255,0) 100%);
  }
  .headline {
    position: absolute;
    left: 638px;
    top: 52px;
    margin: 0;
    font-family: "Montserrat", Arial, sans-serif;
    font-weight: 800;
    font-size: 78px;
    line-height: 72px;
    letter-spacing: 0.5px;
    text-transform: uppercase;
    color: var(--white);
    background: linear-gradient(180deg, var(--white) 0%, var(--white) 62%, var(--silver) 100%);
    -webkit-background-clip: text;
    background-clip: text;
    -webkit-text-fill-color: transparent;
    filter: drop-shadow(0 2px 2px rgba(0, 60, 90, 0.25));
  }
  .headline span { display: block; }
  .tagline {
    position: absolute;
    left: 641px;
    top: 223px;
    margin: 0;
    font-size: 22px;
    color: var(--white);
    white-space: nowrap;
  }
  .cta-button {
    position: absolute;
    left: 645px;
    top: 295px;
    width: 395px;
    height: 58px;
    border-radius: 29px;
    background: linear-gradient(180deg, var(--button-top) 0%, var(--button-bottom) 100%);
    box-shadow: inset 0 -3px 0 var(--button-edge), 0 3px 6px rgba(0, 50, 80, 0.3);
    display: flex;
    align-items: center;
    justify-content: center;
    text-decoration: none;
    z-index: 2;
  }
  .cta-button span {
    font-family: "Montserrat", Arial, sans-serif;
    font-weight: 900;
    font-size: 44px;
    letter-spacing: 0.5px;
    color: var(--cta-red);
    -webkit-text-stroke: 1px rgba(255, 255, 255, 0.6);
    text-shadow: 0 2px 0 rgba(140, 20, 20, 0.35);
  }
  .cta-note {
    position: absolute;
    left: 672px;
    top: 356px;
    width: 344px;
    height: 67px;
    box-sizing: border-box;
    border: 1px solid var(--white);
    border-radius: 4px;
    display: flex;
    align-items: center;
    justify-content: center;
    text-align: center;
    font-size: 18px;
    line-height: 21px;
    letter-spacing: 0.5px;
    color: var(--white);
    text-transform: uppercase;
    padding-top: 6px;
  }
</style>
</head>
<body>
  <div class="banner">
    <div class="mascot" role="img" aria-label="Cartoon technician in a white shirt and blue tie smiling and holding a large orange wrench"></div>
    <div class="divider"></div>
    <h1 class="headline"><span>Lesson</span><span>Learned</span></h1>
    <p class="tagline">I will do it better if I have to do it again</p>
    <a class="cta-button" href="#"><span>CLICK HERE</span></a>
    <div class="cta-note">To learn more about<br>Lesson Learned</div>
  </div>
</body>
</html>
```